Business Card Design for a Lending Business (Hard Money loans)

We need a business card for our Real Estate Lending business. We do hard Money loans for real estate investors. We have an existing logo we like, see attached. I'd like the business card to mostly include the logo colors, but a bright color pop of some sort would be nice to see also. Card should include Logo, Company Name, Company Address, Employee Name, Cell Phone, Main Phone, Email, Website

Industry/Entity Type

Finance / Lending

Contact Information for Business Card

Logo, Company Name, Company Address, Employee Name, Cell Phone, Main Phone, Email, Website

Requirements
Nice to have
• I'd like the business card to mostly include the logo colors, but a bright color pop of some sort would be nice to see also.

```html
<!DOCTYPE html>
<html lang="en">
<head>
<meta charset="utf-8">
<title>Keystone Lending – Business Cards</title>
<link href="https://fonts.googleapis.com/css2?family=Montserrat:wght@500;600&display=swap" rel="stylesheet">
<style>
  :root {
    --navy: #0b2a8f;
    --navy-deep: #0a2796;
    --navy-soft: #2d4aa8;
    --cyan: #1aa3dc;
    --paper: #ffffff;
    --backdrop: #2e2f31;
  }
  * { margin: 0; padding: 0; box-sizing: border-box; }
  html, body { width: 1200px; height: 900px; overflow: hidden; }
  body {
    background: var(--backdrop);
    font-family: "Montserrat", Arial, sans-serif;
    position: relative;
  }
  .card {
    position: absolute;
    width: 540px;
    height: 309px;
    overflow: hidden;
  }
  .card--front { background: var(--paper); color: var(--navy); }
  .card--back { background: var(--navy-deep); }
  .pos-tl { left: 45px; top: 126px; }
  .pos-tr { left: 615px; top: 126px; }
  .pos-bl { left: 45px; top: 465px; }
  .pos-br { left: 615px; top: 465px; }

  .brand {
    position: absolute;
    display: flex;
    align-items: center;
    gap: 10px;
  }
  .brand__dot {
    width: 30px; height: 30px; border-radius: 50%;
    background: var(--cyan);
    flex: none;
  }
  .brand__name {
    font-weight: 600;
    font-size: 19px;
    letter-spacing: 2.5px;
    line-height: 1.15;
    text-transform: uppercase;
    color: var(--navy);
  }
  .brand--left { left: 40px; top: 70px; }
  .brand--right { right: 34px; top: 70px; flex-direction: row-reverse; text-align: right; }
  .brand--back { left: 340px; top: 128px; }
  .brand--back .brand__name { color: var(--paper); }
  .brand--back .brand__dot { background: var(--paper); }

  .person { position: absolute; top: 152px; }
  .person__name { font-weight: 600; font-size: 19px; letter-spacing: 0.3px; color: var(--navy); }
  .person__title { font-weight: 500; font-size: 14px; letter-spacing: 0.4px; color: var(--cyan); margin-top: 2px; }
  .person__rule { width: 43px; height: 3px; background: var(--navy); margin-top: 18px; }

  .contacts { position: absolute; top: 224px; list-style: none; }
  .contacts li {
    display: flex; align-items: center; gap: 7px;
    font-weight: 500; font-size: 14px; line-height: 17.5px; color: var(--navy);
  }
  .contacts svg { width: 13px; height: 13px; flex: none; }

  .address {
    position: absolute; top: 224px;
    font-weight: 500; font-size: 14px; line-height: 17.5px; color: var(--navy);
  }
  .address .web { color: var(--cyan); }
  .address--right { text-align: right; right: 32px; }
  .address--left { left: 40px; }

  .left-col { left: 40px; }
  .right-col { left: 312px; }

  .mark-area {
    position: absolute; left: 0; top: 0; width: 300px; height: 309px;
    background: linear-gradient(90deg, #3c5bb1 0%, #1e3ea0 55%, var(--navy-deep) 100%);
    opacity: 0.75;
  }
  .pattern-area {
    position: absolute; inset: 0;
    background: #15339a;
  }
  .back-tag {
    position: absolute; right: 22px; bottom: 40px;
    font-weight: 600; font-size: 12px; letter-spacing: 2px;
    text-transform: uppercase; color: var(--paper);
  }
</style>
</head>
<body>

<!-- Front, logo left -->
<section class="card card--front pos-tl">
  <div class="brand brand--left">
    <span class="brand__dot"></span>
    <span class="brand__name">Keystone<br>Lending</span>
  </div>
  <div class="person right-col">
    <p class="person__name">DANIEL MORROW</p>
    <p class="person__title">MANAGING DIRECTOR</p>
    <div class="person__rule"></div>
  </div>
  <p class="address address--left">48 Sample Avenue<br>Lakeview, New York 10521<br><span class="web">www.keystonelend.com</span></p>
  <ul class="contacts right-col">
    <li><svg viewBox="0 0 14 14"><circle cx="7" cy="7" r="6.3" fill="none" stroke="#1aa3dc" stroke-width="1.2"/><rect x="5" y="3.5" width="4" height="7" rx="0.8" fill="none" stroke="#0b2a8f" stroke-width="1"/></svg>555 010 22 47</li>
    <li><svg viewBox="0 0 14 14"><circle cx="7" cy="7" r="6.3" fill="none" stroke="#1aa3dc" stroke-width="1.2"/><path d="M4 6.5 Q7 3.5 10 6.5 L9 8 L7.8 7 H6.2 L5 8 Z" fill="#0b2a8f"/></svg>800 555 01 36</li>
    <li><svg viewBox="0 0 14 14"><circle cx="7" cy="7" r="6.3" fill="#1aa3dc"/><rect x="4" y="5" width="6" height="4" fill="#fff"/><path d="M4 5 L7 7.3 L10 5" fill="none" stroke="#1aa3dc" stroke-width="0.8"/></svg>info@keystonelend.com</li>
  </ul>
</section>

<!-- Front, logo right -->
<section class="card card--front pos-tr">
  <div class="brand brand--right">
    <span class="brand__dot"></span>
    <span class="brand__name">Keystone<br>Lending</span>
  </div>
  <div class="person left-col">
    <p class="person__name">DANIEL MORROW</p>
    <p class="person__title">MANAGING DIRECTOR</p>
    <div class="person__rule"></div>
  </div>
  <ul class="contacts left-col">
    <li><svg viewBox="0 0 14 14"><circle cx="7" cy="7" r="6.3" fill="none" stroke="#1aa3dc" stroke-width="1.2"/><rect x="5" y="3.5" width="4" height="7" rx="0.8" fill="none" stroke="#0b2a8f" stroke-width="1"/></svg>555 010 22 47</li>
    <li><svg viewBox="0 0 14 14"><circle cx="7" cy="7" r="6.3" fill="none" stroke="#1aa3dc" stroke-width="1.2"/><path d="M4 6.5 Q7 3.5 10 6.5 L9 8 L7.8 7 H6.2 L5 8 Z" fill="#0b2a8f"/></svg>800 555 01 36</li>
    <li><svg viewBox="0 0 14 14"><circle cx="7" cy="7" r="6.3" fill="#1aa3dc"/><rect x="4" y="5" width="6" height="4" fill="#fff"/><path d="M4 5 L7 7.3 L10 5" fill="none" stroke="#1aa3dc" stroke-width="0.8"/></svg>info@keystonelend.com</li>
  </ul>
  <p class="address address--right">48 Sample Avenue<br>Lakeview, New York 10521<br><span class="web">www.keystonelend.com</span></p>
</section>

<!-- Back, large mark -->
<section class="card card--back pos-bl">
  <div class="mark-area" role="img" aria-label="Large faint brand monogram decoration"></div>
  <div class="brand brand--back">
    <span class="brand__dot"></span>
    <span class="brand__name">Keystone<br>Lending</span>
  </div>
</section>

<!-- Back, pattern -->
<section class="card card--back pos-br">
  <div class="pattern-area" role="img" aria-label="Repeating pattern of the brand monogram in muted blue"></div>
  <span class="back-tag">Keystone Lending</span>
</section>

</body>
</html>
```